Design an App Mockup for Restaurant

Design:

I have built a mobile app for my client. I require 5 mobile screens to be designed.

Please see the attached files for description and guidelines.

I have attached a picture of my clients logo to provide ideas for the colour scheme.

Please let me know if you have any questions.

```html
<!DOCTYPE html>
<html lang="en">
<head>
<meta charset="utf-8">
<title>Vespera – Splash Screen</title>
<link rel="stylesheet" href="https://fonts.googleapis.com/css2?family=Open+Sans:wght@400;600&display=swap">
<style>
  :root {
    --wood-dark: #2a1d15;
    --wood-mid: #4a3628;
    --wood-light: #5c4535;
    --plank-seam: rgba(15, 9, 5, 0.55);
    --text-light: #f4f1ec;
    --text-soft: #e6e0d8;
    --spoon-light: #c8782f;
    --spoon-dark: #8a5a36;
    --leaf-green: #6f8a3a;
    --chili-red: #b3151b;
    --flour-white: #f2efe9;
  }
  * { margin: 0; padding: 0; box-sizing: border-box; }
  html, body {
    width: 687px;
    height: 1200px;
    overflow: hidden;
    background: var(--wood-dark);
    font-family: "Open Sans", "Helvetica Neue", Arial, sans-serif;
  }
  .splash {
    position: relative;
    width: 687px;
    height: 1200px;
    overflow: hidden;
  }
  .wood-background {
    position: absolute;
    inset: 0;
    background: linear-gradient(90deg, var(--wood-dark) 0%, var(--wood-mid) 30%, var(--wood-light) 55%, var(--wood-mid) 80%, var(--wood-dark) 100%);
  }
  .plank-seams {
    position: absolute;
    inset: 0;
  }
  .status-bar {
    position: absolute;
    top: 14px;
    left: 0;
    width: 100%;
    height: 36px;
    color: var(--text-light);
    font-size: 22px;
    display: flex;
    align-items: center;
    justify-content: space-between;
    padding: 0 20px;
    z-index: 3;
  }
  .status-left, .status-right { display: flex; align-items: center; gap: 8px; }
  .status-time {
    position: absolute;
    left: 50%;
    transform: translateX(-50%);
    font-weight: 600;
  }
  .prop {
    position: absolute;
    border-radius: 50%;
    z-index: 1;
  }
  .prop-spoon-leaves {
    left: 6px; top: 11px; width: 277px; height: 296px;
    background: radial-gradient(ellipse at 55% 40%, var(--leaf-green) 0%, var(--spoon-dark) 45%, rgba(74, 54, 40, 0) 72%);
  }
  .prop-chilies {
    left: 450px; top: 179px; width: 216px; height: 192px;
    background: radial-gradient(ellipse at 55% 45%, var(--chili-red) 0%, rgba(179, 21, 27, 0.55) 35%, rgba(74, 54, 40, 0) 70%);
  }
  .prop-spoon-flour {
    left: 67px; top: 803px; width: 312px; height: 336px;
    background: radial-gradient(ellipse at 40% 35%, var(--flour-white) 0%, rgba(242, 239, 233, 0.35) 18%, var(--spoon-light) 40%, rgba(74, 54, 40, 0) 72%);
  }
  .brand {
    position: absolute;
    top: 420px;
    left: 0;
    width: 100%;
    text-align: center;
    color: var(--text-light);
    z-index: 2;
  }
  .brand-name {
    font-size: 84px;
    font-weight: 600;
    line-height: 1;
    letter-spacing: 1px;
  }
  .brand-tagline {
    margin-top: 14px;
    font-size: 23px;
    font-weight: 400;
    color: var(--text-soft);
    display: flex;
    justify-content: center;
    gap: 62px;
  }
  .loading {
    position: absolute;
    top: 636px;
    left: 0;
    width: 100%;
    display: flex;
    justify-content: center;
    align-items: center;
    gap: 16px;
    color: var(--text-soft);
    font-size: 22px;
    z-index: 2;
  }
</style>
</head>
<body>
<main class="splash">
  <div class="wood-background" role="img" aria-label="Dark weathered wooden plank tabletop"></div>
  <svg class="plank-seams" width="687" height="1200" aria-hidden="true">
    <g stroke="var(--plank-seam)" stroke-width="3">
      <line x1="60" y1="0" x2="60" y2="1200"/>
      <line x1="150" y1="0" x2="150" y2="1200"/>
      <line x1="245" y1="0" x2="245" y2="1200"/>
      <line x1="315" y1="0" x2="315" y2="1200"/>
      <line x1="410" y1="0" x2="410" y2="1200"/>
      <line x1="500" y1="0" x2="500" y2="1200"/>
      <line x1="590" y1="0" x2="590" y2="1200"/>
    </g>
  </svg>

  <header class="status-bar">
    <div class="status-left">
      <svg width="68" height="14" aria-hidden="true">
        <circle cx="7" cy="7" r="6" fill="var(--text-light)"/>
        <circle cx="21" cy="7" r="6" fill="var(--text-light)"/>
        <circle cx="35" cy="7" r="6" fill="var(--text-light)"/>
        <circle cx="49" cy="7" r="5.3" fill="none" stroke="var(--text-light)" stroke-width="1.4"/>
        <circle cx="62" cy="7" r="5.3" fill="none" stroke="var(--text-light)" stroke-width="1.4"/>
      </svg>
      <span class="carrier">NOVA</span>
      <svg width="24" height="18" viewBox="0 0 24 18" aria-hidden="true">
        <path d="M2 6 A14 14 0 0 1 22 6" fill="none" stroke="var(--text-light)" stroke-width="2.4"/>
        <path d="M6 10 A8.5 8.5 0 0 1 18 10" fill="none" stroke="var(--text-light)" stroke-width="2.4"/>
        <circle cx="12" cy="15" r="2.4" fill="var(--text-light)"/>
      </svg>
    </div>
    <span class="status-time">4:21 PM</span>
    <div class="status-right">
      <svg width="12" height="20" viewBox="0 0 12 20" aria-hidden="true">
        <path d="M1 5 L11 14 L6 19 L6 1 L11 6 L1 15" fill="none" stroke="rgba(244,241,236,0.6)" stroke-width="1.5"/>
      </svg>
      <span class="battery-level">22%</span>
      <svg width="50" height="20" viewBox="0 0 50 20" aria-hidden="true">
        <rect x="1" y="2" width="43" height="16" rx="3" fill="none" stroke="var(--text-light)" stroke-width="1.6"/>
        <rect x="3.5" y="4.5" width="9" height="11" rx="1.5" fill="var(--text-light)"/>
        <rect x="45.5" y="7" width="3" height="6" rx="1" fill="var(--text-light)"/>
      </svg>
    </div>
  </header>

  <div class="prop prop-spoon-leaves" role="img" aria-label="Carved wooden spoon resting on bay leaves"></div>
  <div class="prop prop-chilies" role="img" aria-label="Two red chili peppers"></div>
  <div class="prop prop-spoon-flour" role="img" aria-label="Wooden spoon beside a scattering of flour"></div>

  <section class="brand">
    <h1 class="brand-name">Vespera</h1>
    <p class="brand-tagline"><span>Fine dining</span><span>Italian pizza</span></p>
  </section>

  <div class="loading">
    <svg width="22" height="22" viewBox="0 0 22 22" aria-hidden="true">
      <g fill="var(--text-soft)">
        <circle cx="11" cy="2.5" r="1.6"/>
        <circle cx="17" cy="5" r="1.4" opacity="0.85"/>
        <circle cx="19.5" cy="11" r="1.4" opacity="0.75"/>
        <circle cx="17" cy="17" r="1.4" opacity="0.65"/>
        <circle cx="11" cy="19.5" r="1.4" opacity="0.55"/>
        <circle cx="5" cy="17" r="1.4" opacity="0.45"/>
        <circle cx="2.5" cy="11" r="1.4" opacity="0.35"/>
        <circle cx="5" cy="5" r="1.4" opacity="0.25"/>
      </g>
    </svg>
    <span>Initializing Service</span>
  </div>
</main>
</body>
</html>
```